Software company seeking fresh website design

Using an already existing logo create a fresh, clean and professional web design for our company "Nimbra Works". Nimbra Works focuses on making business better through system integrations and software product development.

We're looking for a web design which has layouts for the following pages:
- Home Page
- Team Page
- Case Studies
- Market (List of Products)
- Product Page (Individual Product Details)
- About Page
- Media Page

Some websites and designs we'd like you to take inspiration from:
- Quarnel.com
- https://www.plorvate.net/gallery/71830264/Vantrel-redesign
- https://zimmerpost.com/shots/5918304-Bright-Frames-Website-Design-for-a-Software-Company

Ideally the design should communicate an enterprise-level business with years of experience that can be trusted to deliver on budget and on-time.

Target Market(s)

Medium to High-Level Enterprise

Industry/Entity Type

Software Development

Coding

Coded - Design and coding required

Number of Pages Required

5+ page

Font styles to use
Sans Serif

Colors

Designer to choose colors to be used in the design.

Requirements
Must have
• - High Level of Professionalism
• - Be a unique design
• - Come with well-formatted and organised html + css + javascript
• - Must work on ie9, latest Chrome, latest Firefox, latest safari. iPhone6 and Android
• - Must be a progressive template
• - Must incorporate logo colors or at least be compatible with them
Nice to have
• - Hero, an area to display things we're proud of but look good without that area if need be.
• - Juicy animations that are performant and degrade nicely
Should not have
• - Submission must not be a template re-branded for the business

```html
<!DOCTYPE html>
<html lang="en">
<head>
<meta charset="utf-8">
<title>Nimbra Works — Outsourced Software Development</title>
<link rel="stylesheet" href="https://fonts.googleapis.com/css2?family=Poppins:wght@400;500;600;700&family=Open+Sans:wght@400;600&display=swap">
<style>
  :root {
    --white: #ffffff;
    --ink: #2b2b2b;
    --nav-active: #e9546b;
    --hero-deep: #f4673f;
    --hero-mid: #f8845c;
    --hero-light: #fcc1a6;
    --hero-pale: #fde3d6;
    --page: #ffffff;
  }
  * { box-sizing: border-box; margin: 0; padding: 0; }
  html, body { width: 1200px; height: 724px; overflow: hidden; background: var(--page); }
  body { font-family: "Open Sans", Arial, sans-serif; color: var(--ink); position: relative; }

  .site-header {
    position: absolute; top: 0; left: 0; width: 1200px; height: 64px;
    background: var(--white); display: flex; align-items: center; justify-content: space-between;
    padding-left: 40px; z-index: 3; box-shadow: 0 1px 4px rgba(0,0,0,.06);
  }
  .brand { display: flex; align-items: center; gap: 10px; }
  .brand-mark { width: 22px; height: 22px; background: var(--hero-deep); border-radius: 4px; }
  .brand-name { font-family: "Poppins", Arial, sans-serif; font-weight: 600; font-size: 20px; color: var(--hero-deep); }

  .main-nav { display: flex; height: 64px; }
  .main-nav a {
    display: flex; align-items: center; padding: 0 17px; height: 64px;
    font-family: "Poppins", Arial, sans-serif; font-weight: 600; font-size: 13px;
    color: var(--ink); text-decoration: none; letter-spacing: .3px;
  }
  .main-nav a.is-active { background: var(--nav-active); color: var(--white); }

  .hero {
    position: absolute; top: 64px; left: 0; width: 1200px; height: 660px;
    background: linear-gradient(110deg, var(--hero-deep) 0%, var(--hero-mid) 38%, var(--hero-light) 78%, var(--hero-pale) 100%);
    clip-path: polygon(0 0, 100% 0, 100% 58%, 0 100%);
  }
  .hero-content { position: absolute; top: 150px; left: 60px; width: 470px; color: var(--white); z-index: 2; }
  .hero-title { font-family: "Poppins", Arial, sans-serif; font-weight: 700; font-size: 24px; letter-spacing: .5px; margin-bottom: 26px; }
  .hero-text { font-size: 14px; line-height: 1.6; margin-bottom: 28px; }

  .stats { display: grid; grid-template-columns: 1fr 1fr; row-gap: 26px; column-gap: 20px; }
  .stat { display: flex; align-items: center; gap: 10px; }
  .stat-icon { width: 30px; height: 30px; flex: none; }
  .stat-value { font-family: "Poppins", Arial, sans-serif; font-weight: 700; font-size: 26px; line-height: 1; }
  .stat-label { font-size: 12.5px; line-height: 1.25; }

  .hero-visual {
    position: absolute; top: 90px; left: 640px; width: 500px; height: 340px;
    border-radius: 26px; transform: rotate(-14deg);
    background: linear-gradient(160deg, #f4f6f6 0%, #e3ebe8 45%, #5cc28a 100%);
    box-shadow: 0 20px 40px rgba(120,40,10,.25); z-index: 2;
  }
</style>
</head>
<body>
  <header class="site-header">
    <div class="brand">
      <span class="brand-mark"></span>
      <span class="brand-name">Nimbra Works</span>
    </div>
    <nav class="main-nav">
      <a href="#" class="is-active">HOME</a>
      <a href="#">ABOUT</a>
      <a href="#">TEAM</a>
      <a href="#">CASE STUDIES</a>
      <a href="#">MARKET</a>
      <a href="#">PRODUCT</a>
      <a href="#">MEDIA</a>
    </nav>
  </header>

  <section class="hero">
    <div class="hero-content">
      <h1 class="hero-title">OUTSOURCED SOFTWARE DEVELOPMENT</h1>
      <p class="hero-text">Nimbra Works provides end-to-end offshore product development services to various clients, from start-ups to established enterprises, across different industries. We use proven agile methodology to accelerate the development cycle of products from architecture to implementation and deployment.</p>
      <div class="stats">
        <div class="stat">
          <svg class="stat-icon" viewBox="0 0 30 30" fill="none" stroke="#fff" stroke-width="1.6"><rect x="3" y="5" width="24" height="20" rx="2"/><polyline points="7,19 12,13 16,17 23,10"/></svg>
          <span class="stat-value">20+</span><span class="stat-label">Years of Industry<br>Experience</span>
        </div>
        <div class="stat">
          <svg class="stat-icon" viewBox="0 0 30 30" fill="none" stroke="#fff" stroke-width="1.6"><circle cx="15" cy="18" r="7"/><polyline points="10,3 15,11 20,3"/></svg>
          <span class="stat-value">350+</span><span class="stat-label">Projects Delivered</span>
        </div>
        <div class="stat">
          <svg class="stat-icon" viewBox="0 0 30 30" fill="none" stroke="#fff" stroke-width="1.6"><circle cx="15" cy="10" r="5"/><path d="M5 26c1-6 5-9 10-9s9 3 10 9"/></svg>
          <span class="stat-value">500+</span><span class="stat-label">Experts</span>
        </div>
        <div class="stat">
          <svg class="stat-icon" viewBox="0 0 30 30" fill="none" stroke="#fff" stroke-width="1.6"><circle cx="10" cy="11" r="4"/><circle cx="20" cy="11" r="4"/><path d="M3 25c1-5 4-7 7-7s6 2 7 7M13 25c1-5 4-7 7-7s6 2 7 7"/></svg>
          <span class="stat-value">250+</span><span class="stat-label">Customers Served</span>
        </div>
      </div>
    </div>
    <div class="hero-visual" role="img" aria-label="Phone and tablet showing a finance app with a green growth chart"></div>
  </section>
</body>
</html>
```